Harbor LunaVital & Equipments

I need to create full stationery design for the company; Business Card, Envelop, Letterheads, Calendar and email template.

Our company is specialized in the import and export of nutritional, pharmaceutical and cosmetics in addition to medical equipments.

These is no limitation on how to use colors within the design.

Target Market(s)

Global

Industry/Entity Type

Healthcare

Other font styles liked:
• a font close to logo. Letterhead body text to be different than the address text

Requirements
Nice to have
• We will have multiple locations so it is good to keep space for future addresses.
• Stationary requirements:
• Letterhead: A4
• Envelopes: 3 regular sizes : large, medium and small (i do not know the sizes)
• Colors: extracted from the logo

```html
<!DOCTYPE html>
<html lang="en">
<head>
<meta charset="utf-8">
<title>Harbor LunaVital &amp; Equipments – Stationery</title>
<link href="https://fonts.googleapis.com/css2?family=Arimo:wght@400;700&family=Varela+Round&display=swap" rel="stylesheet">
<style>
  :root {
    --brand-blue: #29a9e1;
    --brand-green: #4aa82e;
    --brand-navy: #0b0f5a;
    --paper: #ffffff;
    --backdrop: #ececec;
    --ink: #333333;
    --ink-soft: #666666;
    --edge: #dcdcdc;
  }
  * { box-sizing: border-box; margin: 0; padding: 0; }
  html, body { width: 1200px; height: 937px; overflow: hidden; }
  body {
    background: var(--backdrop);
    position: relative;
    font-family: "Arimo", Arial, sans-serif;
    color: var(--ink);
  }
  .sheet {
    position: absolute;
    background: var(--paper);
    border: 1px solid var(--edge);
    box-shadow: 0 2px 6px rgba(0,0,0,0.08);
  }
  .brand {
    display: flex;
    align-items: center;
    font-family: "Varela Round", "Arimo", sans-serif;
    font-weight: 400;
    color: var(--brand-blue);
    line-height: 1.05;
  }
  .brand-square { background: var(--brand-navy); flex: none; }
  .website {
    position: absolute;
    left: 0; right: 0;
    text-align: center;
    font-size: 9.5px;
    letter-spacing: 3px;
    color: var(--ink);
  }

  /* Letterhead */
  .letterhead { left: 185px; top: 68px; width: 386px; height: 545px; }
  .letterhead .brand { position: absolute; left: 17px; top: 24px; font-size: 16px; gap: 8px; width: 170px; }
  .letterhead .brand-square { width: 26px; height: 26px; border-radius: 3px; }
  .contact-list { position: absolute; left: 315px; top: 22px; list-style: none; font-size: 4.6px; line-height: 8.4px; color: var(--ink-soft); }
  .contact-list li { display: flex; align-items: center; gap: 3px; }
  .contact-list svg { width: 5px; height: 5px; flex: none; }
  .letter { position: absolute; left: 36px; top: 140px; width: 296px; font-size: 5.6px; line-height: 7.6px; color: var(--ink); }
  .letter p { margin-bottom: 9px; }
  .letter .gap-lg { margin-bottom: 18px; }
  .letter strong { font-weight: 700; }
  .signature { display: block; width: 40px; height: 28px; margin: 2px 0 6px; background: linear-gradient(90deg, #e4e4e4, #f4f4f4); }
  .letterhead .website { bottom: 20px; }

  /* Presentation sheet */
  .cover { left: 636px; top: 40px; width: 460px; height: 576px; }
  .cover .brand { position: absolute; left: 0; right: 0; top: 204px; flex-direction: column; gap: 18px; text-align: center; font-size: 42px; }
  .cover .brand-square { width: 86px; height: 86px; border-radius: 8px; }
  .cover .website { bottom: 22px; font-size: 10px; }

  /* Business cards */
  .card { width: 176px; height: 100px; border-radius: 6px; }
  .card-front { left: 46px; top: 658px; }
  .card-back { left: 46px; top: 785px; }
  .card-front .brand { position: absolute; right: 10px; top: 10px; width: 110px; font-size: 10px; gap: 5px; }
  .card-front .brand-square { width: 14px; height: 14px; border-radius: 2px; }
  .card-address { position: absolute; left: 8px; top: 48px; font-size: 3.8px; line-height: 5.6px; color: var(--ink-soft); list-style: none; }
  .card-person { position: absolute; right: 10px; bottom: 8px; text-align: right; font-size: 4.2px; line-height: 5.6px; }
  .card-person .name { color: var(--brand-blue); }
  .card-person .role { color: var(--brand-navy); font-weight: 700; }
  .card-back .brand { position: absolute; left: 0; right: 0; top: 28px; justify-content: center; font-size: 11px; gap: 6px; text-align: left; }
  .card-back .brand-square { width: 16px; height: 16px; border-radius: 2px; }

  /* Envelopes */
  .envelope { width: 441px; height: 207px; }
  .envelope-front { left: 265px; top: 672px; }
  .envelope-front .brand { position: absolute; left: 14px; top: 20px; width: 160px; font-size: 16px; gap: 8px; }
  .envelope-front .brand-square { width: 28px; height: 28px; border-radius: 3px; }
  .envelope-front .website { bottom: 16px; }
  .envelope-back { left: 737px; top: 672px; width: 431px; overflow: hidden; }
  .envelope-flap { position: absolute; left: 0; top: 0; width: 100%; height: 72px; background: var(--brand-navy); border-radius: 0 0 40px 40px; }
  .envelope-back .website { top: 30px; color: #ffffff; font-size: 10px; }
</style>
</head>
<body>

  <section class="sheet letterhead" aria-label="Letterhead">
    <div class="brand"><span class="brand-square"></span><span>Harbor LunaVital &amp; Equipments</span></div>
    <ul class="contact-list">
      <li><svg viewBox="0 0 10 10"><rect width="10" height="10" rx="2" fill="#29a9e1"/></svg>+00 123 4567</li>
      <li><svg viewBox="0 0 10 10"><rect width="10" height="10" rx="2" fill="#29a9e1"/></svg>+00 123 4568</li>
      <li><svg viewBox="0 0 10 10"><rect width="10" height="10" rx="2" fill="#29a9e1"/></svg>+00 123 4569</li>
      <li><svg viewBox="0 0 10 10"><rect width="10" height="10" rx="2" fill="#29a9e1"/></svg>info@harborlunavital.com</li>
      <li><svg viewBox="0 0 10 10"><rect width="10" height="10" rx="2" fill="#29a9e1"/></svg>www.harborlunavital.com</li>
    </ul>
    <div class="letter">
      <p>July 2, 2012</p>
      <p><strong>Dear CR,</strong><br>ABC Building, def St., Country Name</p>
      <p>is simply dummy text of the printing and typesetting industry. Lorem Ipsum has been the industry's standard dummy text ever since the 1500s, when an unknown printer took a galley of type and scrambled it to make a type specimen book. It has survived not only five centuries, but also the leap into electronic typesetting, remaining essentially unchanged. It was popularised in the 1960s with the release of Letraset sheets containing Lorem Ipsum passages, and more recently with desktop publishing software including versions of Lorem Ipsum.</p>
      <p class="gap-lg">is simply dummy text of the printing and typesetting industry. Lorem Ipsum has been the industry's standard dummy text ever since the 1500s, when an unknown printer took a galley of type and scrambled it to make</p>
      <p>is simply dummy text of the printing and typesetting industry. Lorem Ipsum has been the industry's standard dummy text ever since the 1500s, when an unknown printer took a galley of type and scrambled it to make a type specimen book. It has survived not only five centuries, but also the leap into electronic typesetting, remaining essentially unchanged. It was popularised in the 1960s with the release of Letraset sheets containing Lorem Ipsum passages, and more recently with desktop publishing software including versions of Lorem Ipsum.</p>
      <p>Best Regards,</p>
      <span class="signature" role="img" aria-label="Handwritten signature"></span>
      <p><strong>Daniel Reyes</strong><br>Director<br><br>ABC Building, def St., Country Name</p>
    </div>
    <div class="website">www.harborlunavital.com</div>
  </section>

  <section class="sheet cover" aria-label="Presentation sheet">
    <div class="brand"><span class="brand-square"></span><span>Harbor LunaVital<br>&amp; Equipments</span></div>
    <div class="website">www.harborlunavital.com</div>
  </section>

  <section class="sheet card card-front" aria-label="Business card front">
    <div class="brand"><span class="brand-square"></span><span>Harbor LunaVital &amp; Equipments</span></div>
    <ul class="card-address">
      <li>12 Harbor Road</li>
      <li>Suite 4, Country</li>
      <li>+00 123 4567</li>
      <li>+00 123 4568</li>
      <li>info@harborlunavital.com</li>
      <li>www.harborlunavital.com</li>
    </ul>
    <div class="card-person"><div class="name">Daniel Reyes</div><div class="role">General Manager</div></div>
  </section>

  <section class="sheet card card-back" aria-label="Business card back">
    <div class="brand"><span class="brand-square"></span><span>Harbor LunaVital<br>&amp; Equipments</span></div>
  </section>

  <section class="sheet envelope envelope-front" aria-label="Envelope front">
    <div class="brand"><span class="brand-square"></span><span>Harbor LunaVital &amp; Equipments</span></div>
    <div class="website">www.harborlunavital.com</div>
  </section>

  <section class="sheet envelope envelope-back" aria-label="Envelope back">
    <div class="envelope-flap"></div>
    <div class="website">www.harborlunavital.com</div>
  </section>

</body>
</html>
```